Flyer-Design für Immobilienmarketing von Raumfreude Home Staging
Zielgruppe
Wir (Raumfreude Home Staging) geben mit Home Staging Immobilien ein Raumfreude (www.raumfreude-beispiel.de). Ziel ist die Immobilienvermarktung zu beschleunigen (Immobilienmarketing) und den besten Preis zu erzielen. Durch ein eigenes Möbel und Dekolager erfolgt die Gestaltung zeitnah.
Zielgruppe sind Immobilienverkäufer (privat) und auch Makler/Vermittler/Projektentwickler
Aufgabenstellung
Wir benötigen einen Flyer/Klappkarte DIN lang quer. Dieser sollte hochwertig, einladend, hell und freundlich erscheinen. Wenn er an der langen Seite gefaltet ist, sollte er als Klappkarte auf dem Tisch stehen können. Dabei sollen alle 4 Seiten genutzt werden. Logo und Design sowie Kurzbeschreibungen/Texte entsprechend bitte der Website (www.raumfreude-beispiel.de) verwenden. Originale können zur Verfügung gestellt werden. Der Flyer sollte auch als PDF nutzbar sein.
Als Slogan stellen wir uns folgendes vor 'Mit Raumfreude in den Immobilienverkauf starten und beim besten Preis landen', sind aber für alles offen. Bei Verwendung von Referenzen wäre ein Spruch mit 'Wohlfühlen' gut. Des Weiteren einfach bei den Texten und Bildern der Website bedienen (Vorteile + warum mit uns) und einen knackigen überzeugenden Flyer bei dem hauptsächlich die Bilder sprechen, erstellen. Wir freuen uns auf die Vorschläge.

```html
<!DOCTYPE html>
<html lang="de">
<head>
<meta charset="utf-8">
<title>Raumfreude Home Staging – Klappkarte</title>
<link href="https://fonts.googleapis.com/css2?family=Quicksand:wght@400;500;600;700&family=Poppins:wght@300;400&display=swap" rel="stylesheet">
<style>
:root{
  --stage:#e8e8e6;
  --paper:#ffffff;
  --ink:#2f2f2f;
  --ink-soft:#666666;
  --green:#8dbb2a;
  --rule:#555555;
}
*{margin:0;padding:0;box-sizing:border-box}
html,body{width:1200px;height:678px;overflow:hidden;background:var(--stage)}
body{position:relative;font-family:"Poppins",sans-serif;color:var(--ink)}
.spread{position:absolute;left:49px;width:1101px;height:263px;background:var(--paper)}
.spread--outside{top:59px}
.spread--inside{top:357px}
.photo{position:absolute}

/* photo areas: soft gradients in each room's main tones */
.photo--study{background:linear-gradient(172deg,#efebe6 0%,#e6e2dc 30%,#d7d9d2 48%,#c9b8a4 64%,#8c6a4c 82%,#5e432f 100%)}
.photo--lounge{background:linear-gradient(100deg,#e4dcd3 0%,#ddd3c9 35%,#b9bdc2 55%,#8e9db0 70%,#a9b79a 85%,#d9dfd6 100%)}
.photo--open{background:linear-gradient(165deg,#eceae6 0%,#dcdcd6 28%,#a9b0a5 45%,#9aa4ad 58%,#8a6a4f 78%,#5a3f2d 100%)}
.photo--kitchen{background:linear-gradient(175deg,#f2f1ee 0%,#dfe2e4 40%,#a9b4bb 62%,#8c7a68 82%,#5f574f 100%)}
.photo--dining{background:linear-gradient(175deg,#f1efec 0%,#e2ded8 38%,#5f7f78 60%,#2f5e5a 76%,#b08a60 100%)}
.photo--sofa{background:linear-gradient(120deg,#3b3a38 0%,#b99a4a 26%,#d9d4cc 48%,#8f9093 72%,#5e5b57 100%)}
.photo--table{background:linear-gradient(175deg,#f3f2f0 0%,#e3e4e5 40%,#a7aeb5 64%,#8a8f95 80%,#a5825f 100%)}

.contact{position:absolute;left:28px;top:82px;font-family:"Quicksand",sans-serif;font-size:5.9px;letter-spacing:.08em;line-height:10px;font-weight:600;color:var(--ink)}
.contact .gap{margin-top:13.5px}
.contact .strong{font-weight:700}

.claim{position:absolute;left:934px;top:50px;font-family:"Quicksand",sans-serif}
.claim__lead{font-size:12.3px;line-height:13.5px;font-weight:400;color:var(--ink);letter-spacing:.02em}
.claim__accent{font-size:14.6px;line-height:17px;font-weight:700;color:var(--green);margin-top:3px}
.claim__rule{position:absolute;left:934px;top:122px;width:62px;height:1.2px;background:var(--rule)}
.brand{position:absolute;left:932px;top:172px;font-family:"Quicksand",sans-serif;font-size:26px;font-weight:500;color:var(--ink);display:flex;align-items:center;gap:7px}
.brand__dot{width:8px;height:8px;border-radius:50%;background:var(--green)}

.mission{position:absolute;left:41px;top:48px;width:154px;height:167px;display:flex;align-items:center;justify-content:center}
.mission svg{position:absolute;inset:0}
.mission p{position:relative;width:128px;text-align:center;font-size:5.5px;line-height:10.7px;color:var(--ink)}

.service{position:absolute;top:16px}
.service .photo{position:relative;height:100px}
.service h2{font-family:"Quicksand",sans-serif;font-weight:400;font-size:10.4px;letter-spacing:.03em;color:var(--ink-soft);margin:14px 0 0 6px;white-space:nowrap}
.service hr{border:0;height:.8px;background:var(--ink-soft);margin:6px 0 0 6px;width:88px}
.service .body{margin:7px 0 0 6px;font-size:4.9px;line-height:8.8px;width:86px}
.service ul{list-style:none;margin:8px 0 0 6px;font-size:4.9px;line-height:10.6px}
.service li::before{content:"• "}
</style>
</head>
<body>

<section class="spread spread--outside">
  <div class="contact">
    <p>Lena Hartwig</p>
    <p>Lindenallee 12</p>
    <p>20000 Musterstadt</p>
    <p class="gap strong">PH. 040/123 456 78</p>
    <p class="gap strong">info@raumfreude-beispiel.de</p>
    <p class="gap strong">www.raumfreude-beispiel.de</p>
  </div>
  <div class="photo photo--study" style="left:133px;top:15px;width:232px;height:231px" role="img" aria-label="Helles Arbeitszimmer mit Schreibtisch, Regal, Pflanze und Balkonfenstern über Holzboden"></div>
  <div class="photo photo--lounge" style="left:379px;top:15px;width:530px;height:231px" role="img" aria-label="Wohnzimmer mit Sofa, Couchtisch, blauen Sesseln und großer Fensterfront zur begrünten Terrasse"></div>
  <div class="claim">
    <p class="claim__lead">Mit Raumfreude<br>in den Immobilienverkauf</p>
    <p class="claim__accent">starten und beim<br>besten Preis landen'</p>
  </div>
  <div class="claim__rule"></div>
  <div class="brand"><span>Raumfreude</span><span class="brand__dot"></span></div>
</section>

<section class="spread spread--inside">
  <div class="mission">
    <svg width="154" height="167" viewBox="0 0 154 167" fill="none" stroke="#2f2f2f" stroke-width=".8">
      <polyline points="36,0.4 0.4,0.4 0.4,166.6 36,166.6"/>
      <polyline points="118,0.4 153.6,0.4 153.6,166.6 118,166.6"/>
    </svg>
    <p>Unser Ziel ist, die uns anvertraute Immobilie schnell und ganzheitlich so zu gestalten, dass sie alle Sinne eines gemeinsam definierten Zielkunden anspricht. Auf diese Weise ist Home Staging ein wertvolles Instrument der Verkaufs- förderung. Mit einem durchgängigen Konzept, welches sich durch die ganze Immobilie zieht, schaffen wir den optimalen ersten Eindruck und beeinflussen die Kaufentscheidung positiv. Mit unserem Qualitätsanspruch inszenieren wir Wohnräume als Wohnträume.</p>
  </div>
  <div class="photo photo--open" style="left:227px;top:16px;width:411px;height:230px" role="img" aria-label="Offener Wohnbereich mit Sesseln, Pflanzen, Leiterregal, Kamin und Essplatz am Fenster"></div>

  <article class="service" style="left:652px;width:99px">
    <div class="photo photo--kitchen" role="img" aria-label="Wohn- und Essbereich mit offener Küche"></div>
    <h2>HOME STAGING</h2><hr>
    <p class="body">Sie möchten Ihre Immobilie schnell und zum bestmöglichen Preis verkaufen? Wir gestalten Ihre Immobilie zielgerich- tet als das Zuhause, nach dem Käufer suchen.</p>
    <ul><li>Häuser und Ferienhäuser</li><li>Eigentums- und Ferienwohnungen</li><li>Musterwohnungen- häuser</li></ul>
  </article>
  <article class="service" style="left:763px;width:99px">
    <div class="photo photo--dining" role="img" aria-label="Küche mit Esstisch und grünen Samtstühlen"></div>
    <h2>MIETMÖBEL</h2><hr>
    <p class="body">Mieten oder leasen Sie unsere Möbel, Lampen und Wohnaccessoires und genießen Sie ein ansprechendes Event, Büro oder Zuhause auf Zeit.</p>
    <ul><li>Möbel und Wohnaccessoires</li><li>Lampen und Teppiche</li><li>Vorhänge und Plissees</li></ul>
  </article>
  <article class="service" style="left:881px;width:92px">
    <div class="photo photo--sofa" role="img" aria-label="Wohnzimmer mit grauem Sofa und goldenem Wandbild"></div>
    <h2 style="letter-spacing:-.02em">PRIVATE SHOPPING</h2><hr>
    <p class="body">Planen und gestalten Sie Ihr Zuhause mit unserem kreativen Interior-Design-Team und bestellen Sie bei uns Ihre ausgewählten Möbel und Wohnaccessoires.</p>
    <ul><li>Ideen und Wünsche</li><li>Persönliche Beratung</li><li>Design-Vorschlag</li><li>Individuelle Möbelauswahl</li></ul>
  </article>
  <article class="service" style="left:984px;width:99px">
    <div class="photo photo--table" role="img" aria-label="Essbereich mit Stühlen vor offener Küche"></div>
    <h2>INSTANT HOME</h2><hr>
    <p class="body">Wir richten Ihre Immobilie komplett und in kurzer Zeit mit einem individuellen Raumfreude für Sie ein - zum sofort Wohlfühlen und Einziehen.</p>
    <ul><li>Wohnungen und Häuser</li><li>Zweit- und möblierte Wohnungen</li><li>Ferienwohnungen und -häuser</li></ul>
  </article>
</section>

</body>
</html>
```